Aggressive Appliance retailer requires a Large Billboard design.

We require a large Tall billboard design it stands 4500mm high x 2400mm across. We have our own range of imported appliances called Velocane and we provide a 5 year warranty, key pionts low price + long solid warranty. Provided are 3 products 1 x clothes washer 8 kg $699 1 x dishwasher $499 1 x side by side fridge freezer $1299 all with 5 year warranty. Company colors very bright green. Provided warranty logo / images / and an add that has the font we have preference too. I am not rigid to the above requirements and open to designers own ideas :-) I have supplied a few dishwasher images if you want one with closed door i may need to sort one out

```html
<!DOCTYPE html>
<html lang="en">
<head>
<meta charset="utf-8">
<title>Velocane Appliances – Tall Billboard</title>
<link rel="stylesheet" href="https://fonts.googleapis.com/css2?family=Open+Sans:wght@700;800&display=swap">
<style>
  :root {
    --bg: #2b1a12;
    --white: #ffffff;
    --ink: #111111;
    --green-bright: #8fdc1e;
    --green-mid: #4fa51a;
    --green-deep: #1f5a10;
    --burst: #0a0a0a;
    --price: #ffd21a;
    --steel-light: #e4e6e8;
    --steel-dark: #9a9ea3;
  }
  * { margin: 0; padding: 0; box-sizing: border-box; }
  html, body { width: 1200px; height: 1000px; overflow: hidden; }
  body {
    background: var(--bg);
    font-family: "Open Sans", Arial, sans-serif;
    position: relative;
  }
  .billboard {
    position: absolute;
    left: 360px; top: 51px;
    width: 480px; height: 898px;
    background: var(--white);
    overflow: hidden;
    box-shadow: 0 6px 24px rgba(0,0,0,0.5);
  }
  .brand {
    position: absolute;
    left: 0; top: 0; width: 480px; height: 223px;
    display: flex; flex-direction: column; align-items: center; justify-content: center;
    color: var(--ink);
    font-weight: 800;
    line-height: 1;
  }
  .brand-name { font-size: 92px; letter-spacing: -2px; }
  .brand-sub { font-size: 34px; letter-spacing: 6px; margin-top: 10px; }
  .promo {
    position: absolute;
    left: 0; top: 223px; width: 480px; height: 574px;
    background: radial-gradient(ellipse at 45% 35%, var(--green-bright) 0%, var(--green-mid) 50%, var(--green-deep) 100%);
  }
  .tagline {
    position: absolute;
    left: 30px; top: 248px;
    color: var(--white);
    font-weight: 800; font-size: 34px; line-height: 0.95;
    text-align: center;
    transform: rotate(-14deg);
    text-shadow: 2px 2px 3px rgba(0,0,0,0.55);
  }
  .product {
    position: absolute;
    border-radius: 6px;
    background: linear-gradient(135deg, var(--steel-light), var(--steel-dark));
    box-shadow: 3px 4px 8px rgba(0,0,0,0.35);
  }
  .product-washer { left: 292px; top: 203px; width: 188px; height: 247px; }
  .product-dishwasher { left: 15px; top: 413px; width: 168px; height: 207px; }
  .product-fridge { left: 308px; top: 545px; width: 148px; height: 278px; }
  .burst {
    position: absolute;
    display: flex; flex-direction: column; align-items: center; justify-content: center;
    color: var(--price);
    font-weight: 800;
    line-height: 1;
  }
  .burst svg { position: absolute; inset: 0; width: 100%; height: 100%; }
  .burst .price { position: relative; font-size: 46px; letter-spacing: -1px; }
  .burst .unit { position: relative; font-size: 13px; align-self: flex-end; margin-right: 58px; }
  .burst-washer { left: 125px; top: 250px; width: 220px; height: 165px; }
  .burst-dishwasher { left: 170px; top: 420px; width: 200px; height: 150px; }
  .burst-fridge { left: 105px; top: 590px; width: 220px; height: 160px; }
  .warranty-badge {
    position: absolute;
    left: 23px; top: 715px; width: 100px; height: 100px;
    border-radius: 10px;
    background: linear-gradient(160deg, var(--steel-light), var(--steel-dark));
    border: 2px solid #6d7175;
  }
  .warranty-note {
    position: absolute;
    left: 128px; top: 757px; width: 140px;
    color: var(--white);
    font-weight: 800; font-size: 14px; line-height: 1.1;
    text-align: center;
    text-shadow: 1px 1px 2px rgba(0,0,0,0.6);
  }
  .retailer {
    position: absolute;
    left: 0; top: 797px; width: 480px; height: 101px;
    display: flex; align-items: center; justify-content: center;
    color: var(--ink);
    font-weight: 700; font-size: 46px; letter-spacing: 0.5px;
  }
</style>
</head>
<body>
  <main class="billboard">
    <header class="brand">
      <span class="brand-name">Velocane</span>
      <span class="brand-sub">APPLIANCES</span>
    </header>

    <section class="promo"></section>

    <div class="tagline">Low<br>Prices!</div>

    <div class="product product-washer" role="img" aria-label="Photo of a silver top-loading 8 kg clothes washer"></div>
    <div class="product product-dishwasher" role="img" aria-label="Photo of a silver freestanding dishwasher"></div>

    <div class="burst burst-washer">
      <svg viewBox="0 0 200 150" preserveAspectRatio="none" aria-hidden="true"><polygon fill="var(--burst)" points="200,75 165.7,87.4 186.6,112.5 148.1,108.9 150,140 117.6,121.4 100,150 82.4,121.4 50,140 51.9,108.9 13.4,112.5 34.3,87.4 0,75 34.3,62.6 13.4,37.5 51.9,41.1 50,10 82.4,28.6 100,0 117.6,28.6 150,10 148.1,41.1 186.6,37.5 165.7,62.6"/></svg>
      <span class="price">$699</span>
      <span class="unit">8 kg</span>
    </div>

    <div class="burst burst-dishwasher">
      <svg viewBox="0 0 200 150" preserveAspectRatio="none" aria-hidden="true"><polygon fill="var(--burst)" points="200,75 165.7,87.4 186.6,112.5 148.1,108.9 150,140 117.6,121.4 100,150 82.4,121.4 50,140 51.9,108.9 13.4,112.5 34.3,87.4 0,75 34.3,62.6 13.4,37.5 51.9,41.1 50,10 82.4,28.6 100,0 117.6,28.6 150,10 148.1,41.1 186.6,37.5 165.7,62.6"/></svg>
      <span class="price">$499</span>
    </div>

    <div class="burst burst-fridge">
      <svg viewBox="0 0 200 150" preserveAspectRatio="none" aria-hidden="true"><polygon fill="var(--burst)" points="200,75 165.7,87.4 186.6,112.5 148.1,108.9 150,140 117.6,121.4 100,150 82.4,121.4 50,140 51.9,108.9 13.4,112.5 34.3,87.4 0,75 34.3,62.6 13.4,37.5 51.9,41.1 50,10 82.4,28.6 100,0 117.6,28.6 150,10 148.1,41.1 186.6,37.5 165.7,62.6"/></svg>
      <span class="price">$1299</span>
    </div>

    <div class="warranty-badge" role="img" aria-label="Five year warranty badge"></div>
    <p class="warranty-note">ALL WITH 5 YEAR WARRANTY!</p>

    <footer class="retailer">Hearthline</footer>

    <div class="product product-fridge" role="img" aria-label="Photo of a silver side-by-side fridge freezer"></div>
  </main>
</body>
</html>
```